I am looking for a modern style design for a podcast cover art.
Titled: Open Harbor with R.K. Thistlewood
colors to stay in the grays, reds, blacks, white, gold, and maybe blues if it fits well. I attached a mock up of what we are going for and a current podcast cover we drew inspiration from.
Colors
3276b5
ec1f27
f04a50
1b1b1b
474747
919191
d2d2d2

```html
<!DOCTYPE html>
<html lang="en">
<head>
<meta charset="utf-8">
<title>Open Harbor with R.K. Thistlewood — Podcast Cover</title>
<link rel="stylesheet" href="https://fonts.googleapis.com/css2?family=Josefin+Sans:wght@700&family=Jost:wght@300&display=swap">
<style>
  :root {
    --page: #ffffff;
    --ink-deep: #111111;
    --ink: #1b1b1b;
    --ink-mid: #474747;
    --gray: #919191;
    --gray-light: #d2d2d2;
    --white: #ffffff;
    --red: #ec1f27;
    --red-dark: #5a0c0f;
    --rust: #4a2012;
    --host-light: #8a8a8a;
    --host-dark: #2b2b2b;
  }
  html, body {
    margin: 0;
    padding: 0;
    width: 1200px;
    height: 1000px;
    overflow: hidden;
    background: var(--page);
  }
  .canvas {
    position: relative;
    width: 1200px;
    height: 1000px;
  }
  .cover {
    position: absolute;
    left: 57px;
    top: 225px;
    width: 1050px;
    height: 572px;
    overflow: hidden;
    background: radial-gradient(ellipse at 40% 45%, #2e2e2e 0%, var(--ink) 60%, var(--ink-deep) 100%);
  }
  .cover svg { display: block; }
  .title-word {
    font-family: "Josefin Sans", sans-serif;
    font-weight: 700;
    letter-spacing: 0.08em;
  }
  .title-word--echo { fill: #262626; stroke: #3a3a3a; stroke-width: 1.5; }
  .title-word--top { fill: var(--white); }
  .title-word--bottom { fill: var(--red); }
  .host-line {
    font-family: "Jost", sans-serif;
    font-weight: 300;
    fill: var(--gray-light);
  }
  .block--red { fill: var(--red-dark); opacity: 0.85; }
  .block--rust { fill: var(--rust); opacity: 0.8; }
  .block--overlay { fill: #7a1216; opacity: 0.6; }
</style>
</head>
<body>
<main class="canvas">
  <section class="cover">
    <svg width="1050" height="572" viewBox="0 0 1050 572" xmlns="http://www.w3.org/2000/svg">
      <defs>
        <linearGradient id="host-tone" x1="0" y1="0" x2="1" y2="1">
          <stop offset="0" stop-color="var(--host-light)"/>
          <stop offset="0.5" stop-color="var(--host-dark)"/>
          <stop offset="1" stop-color="#141414"/>
        </linearGradient>
      </defs>

      <!-- background blocks -->
      <rect class="block--red" x="580" y="55" width="146" height="147"/>
      <rect class="block--red" x="728" y="0" width="145" height="50"/>
      <rect class="block--red" x="905" y="38" width="160" height="210" transform="rotate(8 985 143)"/>
      <rect class="block--rust" x="0" y="443" width="143" height="129"/>
      <rect class="block--rust" x="98" y="395" width="100" height="100"/>
      <rect class="block--rust" x="600" y="412" width="150" height="150" transform="rotate(20 675 487)"/>

      <!-- echo title -->
      <text class="title-word title-word--echo" x="310" y="75" font-size="70" text-anchor="middle" textLength="245" lengthAdjust="spacingAndGlyphs">OPEN</text>
      <text class="title-word title-word--echo" x="310" y="185" font-size="100" text-anchor="middle" textLength="415" lengthAdjust="spacingAndGlyphs">HARBOR</text>

      <!-- host photo area -->
      <rect x="783" y="80" width="267" height="492" fill="url(#host-tone)" role="img" aria-label="Black and white photo of host R.K. Thistlewood in a tuxedo, pointing toward the title"/>

      <rect class="block--overlay" x="895" y="395" width="155" height="160" transform="rotate(10 972 475)"/>

      <!-- main title -->
      <text class="title-word title-word--top" x="308" y="263" font-size="68" text-anchor="middle" textLength="244" lengthAdjust="spacingAndGlyphs">OPEN</text>
      <text class="title-word title-word--bottom" x="308" y="376" font-size="100" text-anchor="middle" textLength="415" lengthAdjust="spacingAndGlyphs">HARBOR</text>

      <!-- host credit -->
      <text class="host-line" x="100" y="525" font-size="32" textLength="430" lengthAdjust="spacingAndGlyphs">with R.K. THISTLEWOOD</text>
    </svg>
  </section>
</main>
</body>
</html>
```